Redesign Website for Corvane Blaze

I have an existing website on https://www.corvaneblaze-demo.com.au/ and would like to have this redesigned professionally with new content (please refer to word document). We are fire protection engineers providing fire services design expertise and engineering design to a range of different clients.

We also provide drafting services to clients in the form of completing final commissioning documentation such as 'as-installed' drawings and fire services block plans to ensure compliance with the building code and relevant Australian Standards.

Target Market(s)

Builders, Architects, Consultants, Project Managers

Industry/Entity Type

Engineering Consultant

Coding

Coded - Design and coding required

Number of Pages Required

4 page

Font styles to use
Sans Serif

Requirements
Must have
• Home and about Page, fire services design page, fire block plans page, contact us page (4 Pages).

The website colour choice must match or compliment the new company logo.
Nice to have
• Quality photos of fire services installations in buildings to Australian Standards.

A website similar to this would be ideal http://quorbelflame-demo.com.au
Should not have
• Stolen licensed photos

```html
<!DOCTYPE html>
<html lang="en">
<head>
<meta charset="utf-8">
<title>Corvane Blaze – Fire Protection Solutions</title>
<link rel="stylesheet" href="https://fonts.googleapis.com/css2?family=Montserrat:wght@500;600&family=Roboto:wght@400;500&display=swap">
<style>
:root{
  --orange:#f7931e;
  --orange-dark:#e9820d;
  --ink:#1b1b1b;
  --text:#333;
  --grey-bg:#f4f4f4;
  --line:#b9b9b9;
  --footer:#050505;
  --white:#fff;
}
*{box-sizing:border-box;margin:0;padding:0}
html,body{width:1200px;height:4216px;overflow:hidden}
body{position:relative;font-family:"Roboto",Arial,sans-serif;color:var(--text);background:var(--white)}
.abs{position:absolute}
h1,h2,h3{font-family:"Montserrat",Arial,sans-serif;font-weight:500;letter-spacing:1px}

/* header */
.site-header{position:absolute;left:0;top:0;width:1200px;height:88px;background:var(--white);z-index:3}
.brand{position:absolute;left:96px;top:18px;display:flex;align-items:center;gap:10px}
.brand-dot{width:30px;height:30px;border-radius:50%;background:var(--orange)}
.brand-name{font-family:"Montserrat",sans-serif;font-weight:600;font-size:22px;color:var(--orange);letter-spacing:1px}
.top-contact{position:absolute;top:12px;display:flex;align-items:center;gap:10px;font-size:16px;font-weight:500;color:var(--ink)}
.round-icon{width:38px;height:38px;border-radius:50%;background:var(--orange);display:flex;align-items:center;justify-content:center}
.main-nav{position:absolute;left:385px;top:62px;width:815px;height:48px;background:var(--orange);display:flex;align-items:center;padding-left:36px;z-index:3;clip-path:polygon(18px 0,100% 0,100% 100%,0 100%)}
.main-nav a{color:var(--white);text-decoration:none;font-family:"Montserrat",sans-serif;font-size:13.5px;font-weight:500;letter-spacing:.5px}
.main-nav .sep{color:var(--white);margin:0 27px;font-size:13px}

/* hero */
.hero{position:absolute;left:0;top:88px;width:1200px;height:606px}
.hero-photo{position:absolute;inset:0;background:linear-gradient(180deg,#6d7073 0%,#8c8f91 45%,#a9aaaa 75%,#8f9091 100%)}
.hero-title{position:absolute;top:205px;width:1200px;text-align:center;color:var(--white);font-size:45px;letter-spacing:2px}
.hero-text{position:absolute;top:272px;left:290px;width:620px;text-align:center;color:var(--white);font-size:15px;line-height:26px}
.hex-btn{position:absolute;z-index:4;height:44px;background:var(--orange);color:var(--white);font-family:"Montserrat",sans-serif;font-size:15px;font-weight:600;display:flex;align-items:center;justify-content:center;clip-path:polygon(14px 0,calc(100% - 14px) 0,100% 50%,calc(100% - 14px) 100%,14px 100%,0 50%)}
.slider-arrow{position:absolute;top:282px;width:42px;height:42px;border-radius:50%;background:#111;display:flex;align-items:center;justify-content:center}
.dots{position:absolute;top:544px;left:565px;display:flex;gap:8px}
.dots span{width:11px;height:11px;border-radius:50%;border:1.5px solid var(--white)}
.dots span.on{background:var(--white)}

/* about */
.section-title{position:absolute;z-index:2;width:1200px;text-align:center;font-size:38px;color:var(--ink)}
.divider{position:absolute;z-index:2;left:515px;width:170px;height:40px}
.about-text{position:absolute;left:135px;width:930px;text-align:center;color:var(--white);font-size:14px;line-height:26px}

/* services */
.services-intro{position:absolute;top:1358px;left:270px;width:660px;text-align:center;font-size:14.5px;line-height:26px;color:var(--ink)}
.svc-label{position:absolute;font-size:15px;font-weight:500;color:var(--ink);line-height:21px}

/* block plans */
.block-body{position:absolute;left:661px;top:2088px;width:440px;color:var(--white);font-size:14px;line-height:26px}

/* work */
.hex{position:absolute;width:214px;height:246px;clip-path:polygon(50% 0,100% 25%,100% 75%,50% 100%,0 75%,0 25%)}

/* form */
.field{position:absolute;z-index:2;background:var(--white);border:1px solid #aaa;font-size:14px;color:#444;padding:20px 0 0 22px}

/* footer */
.site-footer{position:absolute;left:0;top:3826px;width:1200px;height:390px;background:var(--footer);color:var(--white)}
.foot-col{position:absolute;top:88px}
.foot-col h3{font-size:17px;font-weight:600;letter-spacing:.5px}
.foot-col .rule{width:205px;height:1px;background:#777;margin:14px 0 20px}
.foot-col li{list-style:none;font-size:13.5px;line-height:31px}
.contact-row{display:flex;align-items:center;gap:18px;font-size:13.5px;line-height:23px;margin-bottom:16px}
.contact-row .circ{width:42px;height:42px;border-radius:50%;background:#1e1e1e;display:flex;align-items:center;justify-content:center;flex:none}
.social{display:flex;gap:8px}
.social span{width:33px;height:33px;border-radius:50%;border:1.5px solid var(--white)}
.copyright{position:absolute;top:348px;width:1200px;text-align:center;font-size:13px}
</style>
</head>
<body>

<header class="site-header">
  <div class="brand"><span class="brand-dot"></span><span class="brand-name">CORVANE BLAZE</span></div>
  <div class="top-contact" style="left:662px">
    <span class="round-icon"><svg width="18" height="18" viewBox="0 0 24 24"><path fill="#fff" d="M6.6 10.8a15 15 0 0 0 6.6 6.6l2.2-2.2a1 1 0 0 1 1-.25 11.4 11.4 0 0 0 3.6.57 1 1 0 0 1 1 1V20a1 1 0 0 1-1 1A17 17 0 0 1 3 4a1 1 0 0 1 1-1h3.5a1 1 0 0 1 1 1 11.4 11.4 0 0 0 .57 3.6 1 1 0 0 1-.25 1z"/></svg></span>
    +614 00 555 019
  </div>
  <div class="top-contact" style="left:850px">
    <span class="round-icon"><svg width="18" height="14" viewBox="0 0 18 14"><rect x="1" y="1" width="16" height="12" fill="none" stroke="#fff" stroke-width="1.6"/><path d="M1 1l8 7 8-7" fill="none" stroke="#fff" stroke-width="1.6"/></svg></span>
    info@corvaneblaze-demo.com.au
  </div>
</header>
<nav class="main-nav">
  <a href="#">HOME</a><span class="sep">|</span><a href="#">ABOUT</a><span class="sep">|</span><a href="#">FIRE SERVICES DESIGN</a><span class="sep">|</span><a href="#">FIRE BLOCK PLANS</a><span class="sep">|</span><a href="#">CONTACT US</a>
</nav>

<section class="hero">
  <div class="hero-photo" role="img" aria-label="Underground car park with exit sign and yellow painted columns"></div>
  <h1 class="hero-title">FIRE PROTECTION SOLUTIONS</h1>
  <p class="hero-text">We pride ourselves in our ability to meet the demand of our clients and our ability to consistently uphold our 3 key business values in providing our services at quick turnaround, quality service at competitive pricing</p>
  <div class="hex-btn" style="left:517px;top:370px;width:166px">GET STARTED</div>
  <div class="slider-arrow" style="left:25px"><svg width="12" height="18"><path d="M10 2 3 9l7 7" stroke="#fff" stroke-width="2" fill="none"/></svg></div>
  <div class="slider-arrow" style="left:1123px"><svg width="12" height="18"><path d="M2 2l7 7-7 7" stroke="#fff" stroke-width="2" fill="none"/></svg></div>
  <div class="dots"><span class="on"></span><span></span><span></span><span></span></div>
</section>

<section class="about">
  <svg class="abs" style="left:0;top:694px" width="1200" height="492"><polygon points="0,0 1200,0 1200,378 600,486 0,378" fill="#f7931e"/><polyline points="0,378 600,486 1200,378" fill="none" stroke="#9a9a9a" stroke-width="3"/></svg>
  <h2 class="section-title" style="top:764px;color:#fff">ABOUT CORVANE BLAZE</h2>
  <svg class="divider" style="top:822px"><line x1="0" y1="20" x2="68" y2="20" stroke="#fff"/><line x1="102" y1="20" x2="170" y2="20" stroke="#fff"/><circle cx="85" cy="20" r="14" fill="none" stroke="#fff" stroke-width="2"/></svg>
  <p class="about-text" style="top:872px">Corvane Blaze is a company based in Sydney providing the Australian market expertise in the field of fire safety. Our mission is to assist builders, architects, fire contractors, consultants and project managers with the preparation of fire services design and specifications to meet regulatory requirements for Complying Development Certificate (CDC), Development Applications (DA) or Council Fire Orders.</p>
  <p class="about-text" style="top:963px">We also provide fire services design peer review and sign-off under the new Fire Services Design (FSD) class of the Fire Protection Accreditation Scheme (FPAS) and the preparation of a Clause 164B objection letter to exempt certain</p>
  <div class="hex-btn" style="left:519px;top:1038px;width:162px;background:#fff;padding:2px"><div class="hex-btn" style="position:static;width:100%;height:100%;background:var(--orange)">LEARN MORE</div></div>
</section>

<section class="services">
  <h2 class="section-title" style="top:1252px">FIRE SERVICES DESIGN</h2>
  <svg class="divider" style="top:1306px"><line x1="0" y1="20" x2="68" y2="20" stroke="#f7931e"/><line x1="102" y1="20" x2="170" y2="20" stroke="#f7931e"/><circle cx="85" cy="20" r="14" fill="none" stroke="#f7931e" stroke-width="2"/></svg>
  <p class="services-intro">We have proficient knowledge and capabilities in the preparation of fire services design and specifications relating to the below fire safety systems:</p>

  <svg class="abs" style="left:0;top:1420px" width="1200" height="420" fill="none">
    <g stroke="#f7931e" stroke-dasharray="4 4" stroke-width="1.2">
      <polyline points="342,40 490,40 517,80"/>
      <polyline points="268,112 450,112 470,128"/>
      <polyline points="258,262 445,262 470,240"/>
      <polyline points="340,338 485,338 517,298"/>
      <polyline points="823,40 682,40 652,80"/>
      <polyline points="862,112 722,112 700,128"/>
      <polyline points="870,262 725,262 700,240"/>
      <polyline points="826,338 685,338 652,298"/>
      <line x1="584" y1="304" x2="584" y2="348"/>
    </g>
    <polygon points="458,186 521,76 649,76 712,186 649,296 521,296" stroke="#f7931e" stroke-width="12" fill="#fff" stroke-linejoin="round"/>
    <polygon points="478,186 531,94 639,94 692,186 639,278 531,278" fill="#fcdcb4"/>
    <g fill="#fff" stroke="#f7931e" stroke-width="2">
      <circle cx="517" cy="80" r="5"/><circle cx="652" cy="80" r="5"/><circle cx="470" cy="128" r="5"/><circle cx="700" cy="128" r="5"/>
      <circle cx="470" cy="240" r="5"/><circle cx="700" cy="240" r="5"/><circle cx="517" cy="298" r="5"/><circle cx="652" cy="298" r="5"/><circle cx="584" cy="304" r="5"/>
    </g>
    <g stroke="#f7931e" stroke-width="1.8" stroke-linecap="round" stroke-linejoin="round">
      <!-- smoke alarm -->
      <line x1="296" y1="24" x2="328" y2="24"/><path d="M300 24v5a12 8 0 0 0 24 0v-5"/><path d="M304 42l-4 10M312 42v10M320 42l4 10"/>
      <!-- occupant warning speaker -->
      <path d="M262 102h7l10-8v28l-10-8h-7z"/><path d="M284 102a8 8 0 0 1 0 12M288 97a14 14 0 0 1 0 22"/>
      <!-- hose reel -->
      <circle cx="272" cy="262" r="17"/><circle cx="272" cy="262" r="11"/><circle cx="272" cy="262" r="5"/><path d="M289 262h6"/>
      <!-- extinguisher -->
      <rect x="307" y="324" width="14" height="26" rx="3"/><path d="M311 324v-5h6v5M317 319h8l3 5"/><line x1="307" y1="336" x2="321" y2="336"/>
      <!-- smoke detection -->
      <circle cx="855" cy="32" r="12"/><circle cx="855" cy="32" r="5"/><path d="M838 18a22 22 0 0 0 0 28M872 18a22 22 0 0 1 0 28"/>
      <!-- EWIS warning -->
      <path d="M893 88l20 34h-40z"/><line x1="893" y1="100" x2="893" y2="111"/><circle cx="893" cy="116" r="0.8"/>
      <!-- hydrant -->
      <path d="M883 252a9 9 0 0 1 18 0"/><rect x="883" y="252" width="18" height="24"/><rect x="877" y="258" width="6" height="8"/><rect x="901" y="258" width="6" height="8"/><circle cx="892" cy="262" r="3"/><line x1="879" y1="278" x2="905" y2="278"/>
      <!-- emergency lighting -->
      <path d="M849 344a7 7 0 1 1 14 0v6h-14z"/><line x1="848" y1="352" x2="864" y2="352"/><path d="M856 322v-5M843 328l-4-3M869 328l4-3M839 340h-5M873 340h5"/>
      <!-- exit sign -->
      <rect x="563" y="354" width="36" height="34"/><path d="M571 371h16M582 366l5 5-5 5"/>
    </g>
  </svg>
  <div class="svc-label" style="left:176px;top:1448px">Smoke Alarms</div>
  <div class="svc-label" style="left:107px;top:1508px;text-align:right;width:138px">Occupant Warning<br>Systems</div>
  <div class="svc-label" style="left:129px;top:1671px">Fire Hose Reels</div>
  <div class="svc-label" style="left:170px;top:1733px;text-align:right;width:120px">Portable Fire<br>Extinguishers</div>
  <div class="svc-label" style="left:545px;top:1814px">Exit Signs</div>
  <div class="svc-label" style="left:888px;top:1431px">Automatic Smoke<br>Detection &amp; Alarm Systems</div>
  <div class="svc-label" style="left:925px;top:1503px">Emergency Warning &amp;<br>Intercom System (EWIS)</div>
  <div class="svc-label" style="left:924px;top:1672px">Fire Hydrants</div>
  <div class="svc-label" style="left:885px;top:1749px">Emergency Lighting</div>
</section>

<section class="block-plans">
  <svg class="abs" style="left:0;top:1826px" width="1200" height="640">
    <rect x="0" y="494" width="1200" height="146" fill="#f4f4f4"/>
    <polygon points="600,96 1200,0 1200,498 600,638" fill="#f7931e"/>
    <polyline points="600,96 1200,0" stroke="#9a9a9a" stroke-width="3" fill="none"/>
  </svg>
  <div class="abs" role="img" aria-label="Red fire pump controllers and pipework in a plant room" style="left:0;top:1830px;width:601px;height:634px;background:linear-gradient(135deg,#c9c9c6 0%,#9b3a35 40%,#c23a33 60%,#7a7d80 100%);clip-path:polygon(0 0,100% 15%,100% 100%,0 78%)"></div>
  <h2 class="abs" style="left:658px;top:2003px;font-size:38px;color:#fff">FIRE BLOCK PLANS</h2>
  <div class="abs" style="left:661px;top:2066px;width:56px;height:2px;background:#fff"></div>
  <p class="block-body">We can also assist our clients in the preparation commissioning documentation (i.e. zone block plan, fire hydrant block plans, sprinkler block plan) as required for relevant fire safety systems on completion of a project to achieve full compliance with relevant Australian Standards for project handover or for the update of existing outdated / missing block plans.</p>
  <div class="hex-btn" style="left:663px;top:2281px;width:164px;background:#fff;padding:2px"><div class="hex-btn" style="position:static;width:100%;height:100%;background:var(--orange)">LEARN MORE</div></div>
</section>

<section class="work">
  <div class="abs" style="left:0;top:2464px;width:1200px;height:760px;background:var(--grey-bg)"></div>
  <h2 class="section-title" style="top:2528px">OUR WORK</h2>
  <svg class="divider" style="top:2582px"><line x1="0" y1="20" x2="68" y2="20" stroke="#f7931e"/><line x1="102" y1="20" x2="170" y2="20" stroke="#f7931e"/><circle cx="85" cy="20" r="14" fill="none" stroke="#f7931e" stroke-width="2"/></svg>
  <div class="hex" role="img" aria-label="Hydrant booster connection on brick wall" style="left:260px;top:2656px;background:linear-gradient(#a86f52,#7d5a48)"></div>
  <div class="hex" role="img" aria-label="Ceiling services in unfinished building" style="left:494px;top:2656px;background:linear-gradient(#8b8b88,#5c5e60)"></div>
  <div class="hex" role="img" aria-label="Red sprinkler valve assembly" style="left:728px;top:2656px;background:linear-gradient(#d4332e,#8f1e1c)"></div>
  <div class="hex" role="img" aria-label="Empty car park level" style="left:143px;top:2856px;background:linear-gradient(#9fa1a2,#6f7173)"></div>
  <div class="hex" role="img" aria-label="Car park ramp with striped floor markings" style="left:377px;top:2856px;background:linear-gradient(#8d8f90,#5d5f61)"></div>
  <div class="hex" role="img" aria-label="Bright residential corridor" style="left:611px;top:2856px;background:linear-gradient(#e2e2e0,#b4b4b2)"></div>
  <div class="hex" role="img" aria-label="Car park with exit sign and yellow columns" style="left:845px;top:2856px;background:linear-gradient(#a6a8a8,#8a8b6a)"></div>
</section>

<section class="call-back">
  <div class="abs" role="img" aria-label="Faded brick wall with fire hydrant equipment" style="left:0;top:3160px;width:1200px;height:666px;background:linear-gradient(180deg,#e6e6e6 0%,#efefef 50%,#f6f6f6 100%)"></div>
  <svg class="abs" style="left:0;top:3140px" width="1200" height="160"><polygon points="0,0 1200,0 1200,0 600,148 0,28" fill="#f4f4f4"/><polyline points="0,28 600,148 1200,2" fill="none" stroke="#f7931e" stroke-width="3"/></svg>
  <div class="hex-btn" style="left:516px;top:3130px;width:168px">VIEW ALL WORK</div>
  <h2 class="section-title" style="top:3352px">REQUEST A CALL BACK</h2>
  <svg class="divider" style="top:3406px"><line x1="0" y1="20" x2="68" y2="20" stroke="#f7931e"/><line x1="102" y1="20" x2="170" y2="20" stroke="#f7931e"/><circle cx="85" cy="20" r="14" fill="none" stroke="#f7931e" stroke-width="2"/></svg>
  <div class="field" style="left:282px;top:3467px;width:314px;height:53px">Name*</div>
  <div class="field" style="left:604px;top:3467px;width:314px;height:53px">Phone*</div>
  <div class="field" style="left:282px;top:3530px;width:314px;height:53px">Email*</div>
  <div class="field" style="left:604px;top:3530px;width:314px;height:53px">Business*</div>
  <div class="field" style="left:282px;top:3592px;width:636px;height:105px">Comments*</div>
  <div class="hex-btn" style="left:516px;top:3693px;width:168px">SUBMIT</div>
</section>

<footer class="site-footer">
  <div class="abs" style="left:98px;top:110px;display:flex;align-items:center;gap:10px">
    <span style="width:28px;height:28px;border-radius:50%;border:2px solid #fff"></span>
    <span style="font-family:Montserrat,sans-serif;font-weight:500;font-size:23px;letter-spacing:1px">CORVANE BLAZE</span>
  </div>
  <div class="social abs" style="left:101px;top:207px"><span></span><span></span><span></span><span></span></div>
  <div class="foot-col" style="left:346px">
    <h3>OUR SUPPORT</h3><div class="rule"></div>
    <ul><li>Features</li><li>Press</li><li>Careers</li><li>Privacy Policy</li><li>Terms of Service</li></ul>
  </div>
  <div class="foot-col" style="left:598px">
    <h3>QUICK LINKS</h3><div class="rule"></div>
    <ul><li>» Home</li><li>» About</li><li>» Fire services design</li><li>» Fire block plans</li><li>» Contact us</li></ul>
  </div>
  <div class="foot-col" style="left:849px">
    <h3>CONTACT INFO</h3><div class="rule"></div>
    <div class="contact-row"><span class="circ"><svg width="14" height="18" viewBox="0 0 14 18"><path d="M7 1a6 6 0 0 0-6 6c0 4.5 6 10 6 10s6-5.5 6-10a6 6 0 0 0-6-6z" fill="none" stroke="#fff" stroke-width="1.6"/><circle cx="7" cy="7" r="2" fill="#fff"/></svg></span>88 Harbour Lane Sydney<br>NSW 2000</div>
    <div class="contact-row"><span class="circ"><svg width="16" height="16" viewBox="0 0 24 24"><path fill="#fff" d="M6.6 10.8a15 15 0 0 0 6.6 6.6l2.2-2.2a1 1 0 0 1 1-.25 11.4 11.4 0 0 0 3.6.57 1 1 0 0 1 1 1V20a1 1 0 0 1-1 1A17 17 0 0 1 3 4a1 1 0 0 1 1-1h3.5a1 1 0 0 1 1 1 11.4 11.4 0 0 0 .57 3.6 1 1 0 0 1-.25 1z"/></svg></span>+614 00 555 019</div>
    <div class="contact-row"><span class="circ"><svg width="18" height="14" viewBox="0 0 18 14"><rect x="1" y="1" width="16" height="12" fill="#fff"/><path d="M1 1l8 7 8-7" fill="none" stroke="#111" stroke-width="1.4"/></svg></span>info@corvaneblaze-demo.com.au</div>
  </div>
  <p class="copyright">© Corvane Blaze  All Rights Reserved 2021 | Privacy Policy | Terms of Use</p>
</footer>

</body>
</html>
```